Cold brew coffee concept

Web site/logo for cold brew coffee served in a keg tap. Cold brew coffee is a natural energy beverage roasted with fair trade/organic beans. Based in New England. Think- Fresh, Natural, Organic, Pure, Mills, Brick, Wood. Ferncastle Coldbrew.

Target Market(s)

Individuals looking for energy drinks without added sugar or dairy. Coffee connoisseurs.

Industry/Entity Type

Trade

Logo Text

Ferncastle Coldbrew

Number of Pages Required

1 page

Font styles to use
Serif

```html
<!DOCTYPE html>
<html lang="en">
<head>
<meta charset="utf-8">
<title>Ferncastle Coldbrew</title>
<link href="https://fonts.googleapis.com/css2?family=Merienda:wght@400;700&family=Cinzel:wght@400&family=Arvo:wght@400;700&family=Lora:ital@0;1&display=swap" rel="stylesheet">
<style>
:root{
  --wood:#6b4843;
  --wood-dark:#503230;
  --frame:#f4efe2;
  --frame-edge:#e2d9c2;
  --nav:#8c7565;
  --plum:#4a1532;
  --plum-deep:#3a0f27;
  --band:#ebe1cd;
  --cream:#fbf8f1;
  --paper:#e9e2d3;
  --ink:#5e4d40;
  --ink-soft:#8b7a66;
  --burlap:#9a7c62;
  --mocha:#7a5a47;
  --coffee:#3b2418;
  --white:#ffffff;
}
*{box-sizing:border-box;margin:0;padding:0}
html,body{width:810px;height:1200px;overflow:hidden}
body{position:relative;font-family:"Arvo",serif;color:var(--ink)}
.wood-backdrop{position:absolute;inset:0;background:repeating-linear-gradient(90deg,var(--wood) 0 22px,var(--wood-dark) 22px 23px,#76524c 23px 42px,var(--wood-dark) 42px 43px)}
.social{position:absolute;top:18px;left:702px;display:flex;gap:6px}
.social span{width:21px;height:21px;border-radius:50%;background:#a89088;border:1px solid #cdb9ae}
.page{position:absolute;left:128px;top:18px;width:562px;height:1182px;background:var(--frame);border:1px solid var(--frame-edge);box-shadow:0 0 8px rgba(0,0,0,.4)}
.page>*{position:absolute;left:8px;width:544px}
.hero{top:7px;height:213px;background:linear-gradient(120deg,#5a3322 0%,#8a3a1c 35%,#c9b8a4 65%,#3a2a22 100%)}
.brand{position:absolute;left:14px;top:22px;display:flex;align-items:center;gap:8px}
.brand-dot{width:22px;height:22px;border-radius:50%;background:var(--white)}
.brand-name{font-family:"Merienda",serif;font-weight:700;font-size:22px;line-height:1.05;color:var(--white)}
.main-nav{top:220px;height:27px;background:linear-gradient(#9a8373,var(--nav));display:flex;justify-content:space-around;align-items:center;border-bottom:5px solid var(--plum)}
.main-nav a{font-family:"Merienda",serif;font-size:11px;color:var(--white);text-decoration:none;white-space:nowrap}
.main-nav i{width:1px;height:12px;background:#c9b7a8}
.welcome{top:252px;height:62px;background:var(--band);text-align:center;padding-top:19px;box-shadow:inset 0 -3px 4px rgba(0,0,0,.06)}
.welcome p{font-family:"Merienda",serif;font-size:11.5px;color:var(--ink);white-space:nowrap}
.welcome .stars{font-size:6px;line-height:8px;color:#b5a894;letter-spacing:1px;margin-top:3px}
.features{top:314px;height:188px;background:var(--cream)}
.feature{position:absolute;top:12px;width:126px;height:126px;border-radius:50%;display:flex;align-items:center;justify-content:center;font-family:"Merienda",serif;font-size:12.5px;font-weight:700;color:var(--white);box-shadow:0 2px 4px rgba(0,0,0,.25)}
.feature.hot{left:46px;background:radial-gradient(circle at 40% 45%,#e9d6bf,#6d5443 70%,#3d2b20)}
.feature.cold{left:206px;background:radial-gradient(circle at 50% 40%,#b8722e,#3e4a30 70%,#1f2418)}
.feature.bake{left:366px;background:radial-gradient(circle at 45% 40%,#d59a52,#6b3d22 70%,#3a2418)}
.btn-menu{position:absolute;left:219px;top:150px;width:99px;height:25px;background:#232323;color:var(--white);font-size:7px;letter-spacing:1px;font-family:"Arvo",serif;display:flex;align-items:center;justify-content:center;font-weight:700}
.beans{top:502px;height:44px;background:linear-gradient(90deg,#4a2a1a,#6e3f24,#3a2015,#6a3a22,#4a2a1a);border-top:3px solid var(--plum)}
.menu-area{top:546px;height:271px;background:#f1ece2}
.menu-board{position:absolute;left:30px;top:12px;width:473px;height:240px;border:1px solid #d3c9b6;background:var(--paper);display:flex}
.menu-nav{width:151px;height:100%;background:var(--burlap);padding:16px 18px;color:var(--white)}
.menu-nav h3{font-family:"Arvo",serif;font-weight:400;font-size:11.5px;padding-bottom:12px;border-bottom:1px solid #d6c6b4;margin-bottom:14px}
.menu-nav li{list-style:none;font-family:"Merienda",serif;font-size:9.5px;display:flex;justify-content:space-between;line-height:16px;white-space:nowrap}
.menu-nav hr{border:0;border-top:1px solid #d6c6b4;margin:18px 0 14px}
.full-menu{display:inline-block;background:#e6dccd;color:var(--ink);font-size:9.5px;padding:6px 22px 6px 8px;clip-path:polygon(0 0,88% 0,100% 50%,88% 100%,0 100%)}
.menu-cards{flex:1;position:relative}
.card{position:absolute;top:3px;width:153px;height:203px;background:#e5dccb;border:1px solid #d8ceba;padding:14px 16px}
.card.one{left:3px}.card.two{left:161px}
.card svg{display:block;margin:0 auto 14px}
.card hr{border:0;border-top:1px solid #cfc4b0;margin-bottom:12px}
.card li{list-style:none;display:grid;grid-template-columns:1fr 34px 8px;font-family:"Lora",serif;font-size:5.5px;line-height:9.5px;color:#4e3f33;white-space:nowrap}
.card li b{width:6px;height:6px;border:1px solid #9b8f7e;margin-top:2px}
.card-bar{position:absolute;left:0;right:0;bottom:0;height:27px;background:var(--mocha);display:flex;justify-content:flex-end;align-items:center;gap:10px;padding-right:12px;color:#e6dccd;font-size:12px}
.divider-band{top:817px;height:28px;background:#4a2f22;border-top:2px dashed #e9e0cf}
.gallery{top:845px;height:116px;background:var(--cream)}
.shot{position:absolute;top:17px;width:138px;height:75px}
.shot.a{left:45px;background:linear-gradient(135deg,#6b3b1c,#9b6a46,#3a2418)}
.shot.b{left:200px;background:linear-gradient(135deg,#4b3226,#e2a56e,#5a606a)}
.shot.c{left:355px;background:linear-gradient(135deg,#b9c6cc,#f3f4f2,#6a8da0)}
.arrow{position:absolute;top:47px;font-size:13px;color:#222}
.tagline{top:961px;height:40px;background:var(--band);text-align:center;padding-top:11px;font-family:"Merienda",serif;font-style:italic;font-size:12px;color:var(--ink-soft);white-space:nowrap}
.find-us{top:1001px;height:112px;background:var(--cream);text-align:center}
.find-us h2{font-family:"Cinzel",serif;font-weight:400;font-size:30px;letter-spacing:3px;color:#4a4744;margin-top:6px}
.contacts{display:flex;justify-content:space-between;padding:0 22px 0 28px;margin-top:14px}
.contacts div{width:160px;font-size:7.5px;color:#222;font-family:"Arvo",serif;white-space:nowrap}
.contacts strong{display:block;font-size:7px;letter-spacing:.5px;margin:3px 0 4px}
.footer{top:1113px;left:0!important;width:560px!important;height:69px;background:var(--plum-deep);text-align:center;padding-top:26px}
.footer nav{font-size:5.5px;font-weight:700;color:var(--white);display:flex;justify-content:center;gap:9px}
.footer nav .current{color:#c9a96a;font-style:italic}
.footer p{font-size:4.8px;color:#a58f9a;margin-top:11px}
</style>
</head>
<body>
<div class="wood-backdrop" role="img" aria-label="Vertical weathered wood plank background"></div>
<div class="social"><span></span><span></span><span></span><span></span></div>
<div class="page">
  <div class="hero" role="img" aria-label="Photo of cold brew coffee in glass jars with a milk pitcher and coffee beans">
    <div class="brand"><span class="brand-dot"></span><span class="brand-name">Ferncastle<br>coffee</span></div>
  </div>
  <nav class="main-nav"><a>home</a><i></i><a>about our coffee</a><i></i><a>our menu</a><i></i><a>the story of coldbrew</a><i></i><a>contact us</a></nav>
  <section class="welcome"><p>Welcome to Ferncastle Coffee... a natural energy beverage roasted with organic beans.</p><div class="stars">☆☆☆☆☆</div></section>
  <section class="features">
    <div class="feature hot" role="img" aria-label="Photo of a hot latte">hot treats</div>
    <div class="feature cold" role="img" aria-label="Photo of cold brew in a pitcher">coldbrew</div>
    <div class="feature bake" role="img" aria-label="Photo of a muffin">bakery</div>
    <div class="btn-menu">SEE OUR MENU</div>
  </section>
  <div class="beans" role="img" aria-label="Photo of roasted coffee beans"></div>
  <section class="menu-area">
    <div class="menu-board">
      <aside class="menu-nav">
        <h3>COFFEE MENU</h3>
        <ul><li>coldbrew coffee<span>&gt;</span></li><li>coffee specialities<span>&gt;</span></li><li>teas &amp; infusions<span>&gt;</span></li><li>catering<span>&gt;</span></li><li>bakery<span>&gt;</span></li><li>menu on the go<span>&gt;</span></li></ul>
        <hr><span class="full-menu">See full menu</span>
      </aside>
      <div class="menu-cards">
        <div class="card one">
          <svg width="48" height="48" viewBox="0 0 48 48"><circle cx="24" cy="24" r="23" fill="var(--mocha)"/><circle cx="24" cy="24" r="18" fill="none" stroke="#e5dccb" stroke-width="1"/><path d="M15 17h15v9a7 7 0 0 1-7 7h-1a7 7 0 0 1-7-7z" fill="#e5dccb"/><path d="M30 20h3a3 3 0 0 1 0 6h-3" fill="none" stroke="#e5dccb" stroke-width="2"/></svg>
          <hr>
          <ul><li>Coffee<span>$.00</span><b></b></li><li>Decaf Roast<span>$.00</span><b></b></li><li>Macchiato<span>$.00</span><b></b></li><li>Caramel<span>$.00</span><b></b></li><li>Hot Vanilla<span>$.00</span><b></b></li><li>Café Latte<span>$.00</span><b></b></li><li>Cappuccino<span>$.00</span><b></b></li><li>Espresso<span>$.00</span><b></b></li><li>Americano<span>$.00</span><b></b></li><li>Café Mocha<span>$.00</span><b></b></li></ul>
        </div>
        <div class="card two">
          <svg width="48" height="48" viewBox="0 0 48 48"><circle cx="24" cy="24" r="23" fill="var(--mocha)"/><circle cx="24" cy="24" r="18" fill="none" stroke="#e5dccb" stroke-width="1"/><path d="M16 13h16l-3 15h-10z" fill="#e5dccb"/><rect x="23" y="28" width="2" height="7" fill="#e5dccb"/><rect x="18" y="35" width="12" height="2" fill="#e5dccb"/></svg>
          <hr>
          <ul><li>Iced Coffee<span>$.00</span><b></b></li><li>Frosty Mocha<span>$.00</span><b></b></li><li>Coffee Shake<span>$.00</span><b></b></li><li>Frozen Blend<span>$.00</span><b></b></li><li>Iced Tonic<span>$.00</span><b></b></li><li>Café Cooler<span>$.00</span><b></b></li><li>Irish Coffee<span>$.00</span><b></b></li><li>Cream Liqueur<span>$.00</span><b></b></li><li>Brewed Café<span>$.00</span><b></b></li><li>Spiced Latte<span>$.00</span><b></b></li></ul>
        </div>
        <div class="card-bar"><span>&#10094;</span><span style="font-size:8px">|</span><span>&#10095;</span></div>
      </div>
    </div>
  </section>
  <div class="divider-band"></div>
  <section class="gallery">
    <span class="arrow" style="left:17px">&#10094;</span>
    <div class="shot a" role="img" aria-label="Photo of iced cold brew in a jar"></div>
    <div class="shot b" role="img" aria-label="Photo of iced coffee with beans and a straw"></div>
    <div class="shot c" role="img" aria-label="Photo of ice cubes in a glass"></div>
    <span class="arrow" style="left:503px">&#10095;</span>
  </section>
  <div class="tagline">Fresh, natural, and organic... try our Ferncastle Coldbrew</div>
  <section class="find-us">
    <h2>FIND US</h2>
    <div class="contacts">
      <div><svg width="9" height="11" viewBox="0 0 10 12"><path d="M5 0a4 4 0 0 1 4 4c0 3-4 8-4 8S1 7 1 4a4 4 0 0 1 4-4z" fill="#222"/><circle cx="5" cy="4" r="1.5" fill="var(--cream)"/></svg><strong>LOCATION</strong>418 Harbor Lane, Dovermill. 310452</div>
      <div><svg width="10" height="10" viewBox="0 0 10 10"><path d="M2 0l2 2-1 2 3 3 2-1 2 2-2 2C4 10 0 6 0 2z" fill="#222"/></svg><strong>CALL US</strong>+1 555.014.2290</div>
      <div><svg width="11" height="9" viewBox="0 0 11 8"><rect width="11" height="8" fill="#222"/><path d="M0 0l5.5 4.5L11 0" fill="none" stroke="var(--cream)" stroke-width="1"/></svg><strong>EMAIL US</strong>hello@ferncastlecoldbrew.com</div>
    </div>
  </section>
  <footer class="footer">
    <nav><span class="current">HOME</span><span>OUR HISTORY</span><span>OUR MENUS</span><span>GALLERY</span><span>CONTACT US</span></nav>
    <p>Copyright © 2014. Ferncastle Roasting Co. All Rights Reserved | Website Designed and Maintained by Northmill Studio</p>
  </footer>
</div>
</body>
</html>
```